Toronto based company needs a logo and business card design

We are "Brellmont Restoration Corp.". A high rise building restoration company based in Toronto. We specialize in Building Envelope, Parking Garage and Waterproofing repairs. Would like to see designs which use the color Teal, Black and White or Red, Black and White. Prefer to have light color background for the front of the card and dark background for the reverse side. For logo design, we would prefer to see high rise building/s incorporated in it.

Industry/Entity Type

Construction

Logo Text

Brellmont

Font styles to use
Sans Serif

Colors
00a990
ffffff
ec1f27
85acd3
000000

```html
<!DOCTYPE html>
<html lang="en">
<head>
<meta charset="utf-8">
<title>Brellmont Restoration Corp. – Business Card</title>
<link href="https://fonts.googleapis.com/css2?family=Montserrat:wght@300;400;600;800&display=swap" rel="stylesheet">
<style>
  :root{
    --teal:#16b39a;
    --charcoal:#333333;
    --ink:#1f1f1f;
    --grey:#8a8a8a;
    --paper:#ffffff;
    --backdrop:#e3e4e6;
  }
  *{margin:0;padding:0;box-sizing:border-box}
  html,body{width:1200px;height:960px;overflow:hidden}
  body{background:var(--backdrop);font-family:'Montserrat',sans-serif;position:relative}
  .card{position:absolute;left:250px;width:700px;height:400px;overflow:hidden;box-shadow:0 8px 24px rgba(0,0,0,.18)}
  .card-front{top:60px;background:var(--paper)}
  .card-back{top:500px;background:var(--charcoal)}
  .card-shapes{position:absolute;inset:0}

  /* wordmark: one colour, one weight, one square */
  .wordmark{display:flex;align-items:center;gap:14px}
  .wordmark-square{width:40px;height:40px;background:var(--teal);flex:none}
  .wordmark-name{font-weight:800;font-size:22px;line-height:1.15;letter-spacing:.5px;text-transform:uppercase;color:var(--ink)}

  /* front */
  .card-front .wordmark{position:absolute;left:40px;top:104px;width:310px}
  .divider{position:absolute;left:370px;top:96px;width:2px;height:110px;background:var(--ink)}
  .contacts{position:absolute;left:390px;top:100px;list-style:none;font-size:14px;color:var(--ink)}
  .contacts li{display:flex;align-items:center;gap:10px;height:32px}
  .contact-alt{position:absolute;left:540px;top:100px;font-size:14px;color:var(--ink);display:flex;align-items:center;gap:10px;height:32px}
  .icon{width:18px;height:18px;border-radius:4px;background:var(--teal);flex:none}
  .socials{position:absolute;right:36px;top:40px;display:flex;gap:12px}
  .socials span{width:20px;height:20px;border-radius:4px;background:var(--ink)}
  .person{position:absolute;left:40px;top:214px}
  .person-name{font-size:26px;color:var(--ink);font-weight:300;letter-spacing:.5px}
  .person-name strong{color:var(--teal);font-weight:800}
  .person-title{font-size:13px;color:var(--grey);letter-spacing:1px;margin-top:2px}
  .address{position:absolute;left:40px;top:318px;color:var(--paper);font-size:12px;letter-spacing:1px;line-height:1.5}

  /* back */
  .card-back .wordmark{position:absolute;left:0;right:0;top:118px;flex-direction:column;gap:18px;text-align:center}
  .card-back .wordmark-square{width:52px;height:52px}
  .card-back .wordmark-name{color:var(--paper);font-size:34px}
  .tagline{position:absolute;left:390px;top:322px;width:280px;text-align:center;color:var(--paper);font-size:14px}
</style>
</head>
<body>

<section class="card card-front" aria-label="Business card front">
  <svg class="card-shapes" width="700" height="400" viewBox="0 0 700 400">
    <polygon points="440,0 700,0 700,16 458,16" fill="var(--charcoal)"/>
    <polygon points="458,16 700,16 700,22 464,22" fill="var(--teal)"/>
    <polygon points="0,300 420,300 446,278 700,278 700,370 0,370" fill="var(--teal)"/>
    <rect x="0" y="370" width="700" height="6" fill="var(--paper)"/>
    <rect x="0" y="376" width="700" height="24" fill="var(--charcoal)"/>
  </svg>

  <div class="socials"><span></span><span></span><span></span></div>

  <div class="wordmark">
    <div class="wordmark-square"></div>
    <div class="wordmark-name">Brellmont<br>Restoration Corp.</div>
  </div>

  <div class="divider"></div>
  <ul class="contacts">
    <li><span class="icon"></span>(416) 555-0182</li>
    <li><span class="icon"></span>www.brellmontrestore.ca</li>
    <li><span class="icon"></span>office@brellmontrestore.ca</li>
  </ul>
  <div class="contact-alt"><span class="icon"></span>+1 416 555 0147</div>

  <div class="person">
    <div class="person-name"><strong>NAME</strong> SURNAME</div>
    <div class="person-title">YOUR TITLE GOES HERE</div>
  </div>

  <div class="address">
    BRELLMONT RESTORATION CORP.<br>
    STREET NUMBER AND POSTAL CODE GOES HERE.
  </div>
</section>

<section class="card card-back" aria-label="Business card back">
  <svg class="card-shapes" width="700" height="400" viewBox="0 0 700 400">
    <polygon points="0,340 360,340 386,306 700,306 700,366 0,366" fill="var(--teal)"/>
    <rect x="0" y="366" width="700" height="8" fill="var(--paper)"/>
    <rect x="0" y="374" width="700" height="26" fill="var(--teal)"/>
  </svg>

  <div class="wordmark">
    <div class="wordmark-square"></div>
    <div class="wordmark-name">Brellmont<br>Restoration Corp.</div>
  </div>

  <div class="tagline">Your tag lineor website goes here</div>
</section>

</body>
</html>
```